Cat-products company needs smart, yet endearing, business card

We need a business card design for a new, but up-and-running, business based in Honolulu, Hawaii. The business is Purrlane Nest Co. Our first product is the most environmentally-friendly cat grass kit ever seen on the planet. Future products, currently in the R&D phase, will include a variety of exciting cat scratchers. We also do consulting work to help apartment-dwellers make their home more cat-friendly and, in the future, plan on doing full, custom installs of structure to create high walkways for cats.

Target Market(s)

Middle-aged, apartment-dwelling, middle-class workers who own 1 or more cats and who dote on them.

Industry/Entity Type

Pet Care

Contact Information for Business Card

A striking, professional, yet warm and friendly design is what we're after.

Font styles to use
Serif
Sans Serif
Other font styles liked:
• Comfortaa

Colors

Designer to choose colors to be used in the design.

Requirements
Must have
• The company logo: (see attachment)
• The company name: Purrlane Nest Co
• The web address: www.purrlanenestco.example
• Email: support@purrlanenestco.example
• Phone: +1 (808) 555 0172
• Update (Fri Jun 30 3017 7:45pm Hawaii Time) I would like, is possible, uploaded picture of the cat grass kit on the back of the card with some text along the lines of: Purrlane Nest Co - Where The Freshest Kitty Sprouts Begin
Nice to have
• A cat picture, cartoon, real or silhouette that illustrates cats in action and/or relaxing; ie using the apartment space to live, play and relax in and being well-contented.
• Most of the website is done in the font: Comfortaa. It might be nice to continue using this for brand consistency.
Should not have
• Hard-to-read fonts.

```html
<!DOCTYPE html>
<html lang="en">
<head>
<meta charset="utf-8">
<title>Purrlane Nest Co — Business Card</title>
<link href="https://fonts.googleapis.com/css2?family=Open+Sans:wght@400;600;700&display=swap" rel="stylesheet">
<style>
  :root {
    --cocoa: #56342e;
    --marigold: #fdb300;
    --paper: #ffffff;
    --backdrop: #ece7e3;
  }
  * { margin: 0; padding: 0; box-sizing: border-box; }
  html, body { width: 1200px; height: 900px; overflow: hidden; }
  body {
    background: var(--backdrop);
    position: relative;
    font-family: "Open Sans", Arial, sans-serif;
  }

  .card { position: absolute; overflow: hidden; }

  /* Front side */
  .card-front {
    left: 78px; top: 34px; width: 587px; height: 364px;
    background: var(--cocoa);
    color: var(--paper);
  }
  .accent-band {
    position: absolute; right: 0; top: 0; width: 52px; height: 100%;
    background: var(--marigold);
  }
  .accent-dot {
    position: absolute; left: 330px; top: 150px; width: 130px; height: 130px;
    border-radius: 50%;
    background: var(--marigold);
  }
  .holder-name {
    position: absolute; left: 27px; top: 55px;
    font-size: 21px; font-weight: 700; letter-spacing: 0.2px;
  }
  .holder-title {
    position: absolute; left: 27px; top: 80px;
    font-size: 15px; font-weight: 400;
  }
  .contact-list {
    position: absolute; left: 27px; top: 252px; list-style: none;
    font-size: 15px; line-height: 21.5px;
  }
  .contact-list li { display: flex; align-items: center; gap: 6px; }
  .contact-list svg { width: 14px; height: 14px; fill: var(--paper); flex: none; }

  /* Back side */
  .card-back {
    left: 388px; top: 505px; width: 567px; height: 352px;
    background: var(--paper);
    text-align: center;
  }
  .brand-mark {
    position: absolute; left: 0; right: 0; top: 82px;
    display: flex; flex-direction: column; align-items: center; gap: 18px;
  }
  .brand-dot {
    width: 70px; height: 70px; border-radius: 50%; background: var(--marigold);
  }
  .brand-name {
    font-size: 40px; font-weight: 700; color: var(--cocoa); line-height: 1.05;
  }
  .brand-web {
    position: absolute; left: 0; right: 0; top: 308px;
    font-size: 14px; font-weight: 700; color: var(--cocoa);
  }
</style>
</head>
<body>
  <section class="card card-front" aria-label="Business card front">
    <div class="accent-band"></div>
    <div class="accent-dot"></div>
    <h1 class="holder-name">DANIEL KEALOHA</h1>
    <p class="holder-title">Managing Director</p>
    <ul class="contact-list">
      <li>
        <svg viewBox="0 0 24 24" aria-hidden="true"><path d="M6.6 10.8a15.1 15.1 0 0 0 6.6 6.6l2.2-2.2c.3-.3.7-.4 1-.2 1.1.4 2.3.6 3.6.6.6 0 1 .4 1 1V20c0 .6-.4 1-1 1A17 17 0 0 1 3 4c0-.6.4-1 1-1h3.5c.6 0 1 .4 1 1 0 1.3.2 2.5.6 3.6.1.3 0 .7-.2 1z"/></svg>
        +1 (808) 555 0172
      </li>
      <li>
        <svg viewBox="0 0 24 24" aria-hidden="true"><path d="M2 5h20v14H2z M3.5 6.5 12 13l8.5-6.5" stroke="#56342e" stroke-width="1.6"/></svg>
        support@purrlanenestco.example
      </li>
      <li>
        <svg viewBox="0 0 24 24" aria-hidden="true"><circle cx="12" cy="12" r="10"/><path d="M2 12h20M12 2c3 3 3 17 0 20M12 2c-3 3-3 17 0 20" stroke="#56342e" stroke-width="1.6" fill="none"/></svg>
        www.purrlanenestco.example
      </li>
    </ul>
  </section>

  <section class="card card-back" aria-label="Business card back">
    <div class="brand-mark">
      <span class="brand-dot"></span>
      <p class="brand-name">Purrlane Nest Co</p>
    </div>
    <p class="brand-web">www.purrlanenestco.example</p>
  </section>
</body>
</html>
```